Copper Wren (short term rental)

This website will be for a short term rental (lodge h&h) located in a small quant town called Medicine Park and at the entrance of the Tallow Creek Reserve. I am currently in a logo contest and will have the logo soon to use on the website My goal for the website is to highlight the home and area with photographs, text, and possibly a rotating video/slide show of the local area. I will soon have a professional photographer at the home and will upload my own photos to the site with your instructions. I want a booking option for customers to use vs hosting sites like KELZ and lodge h&H. . I would like copperwren.org ( or .com—-appreciate your guidance here) for the web address. And I want it to appear on search engines with words like, medicine park, medicine park rental, rental near Wichita mountains, etc. I hope you can help me. Thanks!

Target Market(s)

Outdoor enthusiasts (bikers, hikers, lakers, etc) festival attendees, hippies.

Industry/Entity Type

Short term rental

Coding

Coded - Design and coding required

Number of Pages Required

1 page

Font styles to use
Serif

Colors
00AB8E
00BBA5
67D7C9
C6EFE9
E9F9F6

Requirements
Must have
• Booking calendar, reviews section, contact us section, brief over view of the area, place to upload my photos

```html
<!DOCTYPE html>
<html lang="en">
<head>
<meta charset="utf-8">
<title>Copper Wren – Short Term Rental</title>
<link href="https://fonts.googleapis.com/css2?family=Poppins:wght@500;600;700&family=Roboto:wght@400;500;700&display=swap" rel="stylesheet">
<style>
:root{
  --green:#17a07f;
  --green-dark:#128a6d;
  --green-light:#1fae8c;
  --ink:#1b1b1b;
  --text:#555;
  --muted:#777;
  --line:#d9d9d9;
  --white:#fff;
}
*{box-sizing:border-box;margin:0;padding:0}
html,body{width:1200px;height:4630px;overflow:hidden;background:var(--white)}
body{font-family:"Roboto",Arial,sans-serif;color:var(--text)}
.page{position:relative;width:1200px;height:4630px;overflow:hidden}
.abs{position:absolute}
.heading{font-family:"Poppins",Arial,sans-serif;font-weight:700;color:var(--ink);line-height:1.2}
.center{left:0;width:1200px;text-align:center}
.rule{position:absolute;height:4px;background:var(--green)}
.photo{position:absolute;display:block}

/* header */
.site-header{position:absolute;left:0;top:0;width:1200px;height:93px;background:var(--white);border-top:4px solid var(--green);box-shadow:0 1px 4px rgba(0,0,0,.08);z-index:2}
.logo{position:absolute;left:108px;top:28px;font-family:"Poppins",Arial,sans-serif;font-weight:700;font-size:25px;color:var(--ink)}
.logo span{color:var(--green)}
.nav{position:absolute;top:39px;font-size:14px;font-weight:500;color:var(--ink);letter-spacing:.2px}
.nav.active::before{content:"";position:absolute;left:0;right:0;top:-10px;height:4px;background:var(--green)}
.search-btn{position:absolute;left:1038px;top:24px;width:48px;height:48px;border-radius:50%;background:var(--green)}

/* hero */
.hero{position:absolute;left:0;top:93px;width:1200px;height:685px;background:linear-gradient(180deg,#c7b9c9 0%,#d9b8a4 22%,#8e7a62 45%,#5e6b43 75%,#3f4b2c 100%)}
.hero-title{position:absolute;top:230px;font-family:"Poppins",Arial,sans-serif;font-weight:700;font-size:86px;line-height:90px;color:var(--white);text-shadow:0 2px 8px rgba(0,0,0,.35)}
.btn{position:absolute;display:flex;align-items:center;justify-content:center;gap:5px;background:var(--green);color:var(--white);font-weight:700;font-size:13px;border-radius:22px;font-family:"Poppins",Arial,sans-serif}
.hero-arrow{position:absolute;top:299px;width:46px;height:46px;border-radius:50%;background:var(--white)}

/* booking */
.booking{position:absolute;left:111px;top:706px;width:977px;height:142px;background:var(--green);border-radius:3px;z-index:1}
.booking label{position:absolute;top:36px;color:var(--white);font-family:"Poppins",Arial,sans-serif;font-weight:600;font-size:13px}
.booking .field{position:absolute;top:66px;height:42px;border:2px solid var(--white)}
.book-now{position:absolute;top:66px;left:726px;width:219px;height:42px;background:var(--white);color:var(--green);font-family:"Poppins",Arial,sans-serif;font-weight:600;font-size:13px;display:flex;align-items:center;justify-content:center}

/* text */
.para{position:absolute;font-size:14px;line-height:25.5px;text-align:justify;color:var(--text)}
.eyebrow{position:absolute;left:596px;top:948px;font-family:"Poppins",Arial,sans-serif;font-weight:600;font-size:15px;letter-spacing:5px;color:var(--green)}

/* property */
.property-band{position:absolute;left:0;top:1483px;width:1200px;height:707px;background:var(--green)}
.card{position:absolute;background:var(--white);border-radius:8px;box-shadow:0 2px 6px rgba(0,0,0,.12)}
.prop-title{position:absolute;left:20px;top:228px;font-family:"Poppins",Arial,sans-serif;font-weight:600;font-size:21px;color:var(--ink)}
.prop-loc{position:absolute;left:20px;top:268px;font-size:14px;color:var(--ink);display:flex;align-items:center;gap:6px}
.prop-desc{position:absolute;left:22px;top:298px;width:275px;font-size:13.5px;line-height:26px;color:var(--text)}
.prop-link{position:absolute;left:22px;top:361px;font-size:13.5px;color:var(--green)}

/* reviews */
.review{position:absolute;top:2396px;width:313px;height:350px;background:var(--white);border-top:4px solid #b9b9b9;box-shadow:0 2px 8px rgba(0,0,0,.12)}
.review.featured{border-top-color:var(--green)}
.quote{position:absolute;left:32px;top:22px;font-family:"Poppins",Arial,sans-serif;font-weight:700;font-size:40px;color:var(--green);line-height:1}
.review p{position:absolute;left:32px;top:70px;width:250px;font-size:13.5px;line-height:25.8px;text-align:justify}
.review hr{position:absolute;left:32px;top:262px;width:250px;border:0;border-top:1px solid var(--line)}
.avatar{position:absolute;left:28px;top:276px;width:54px;height:54px;border-radius:50%;background:linear-gradient(135deg,#9aa7b4,#5b6670)}
.reviewer{position:absolute;left:92px;top:283px;font-family:"Poppins",Arial,sans-serif;font-weight:500;font-size:15px;color:var(--ink)}
.reviewer small{display:block;font-family:"Roboto",Arial,sans-serif;font-size:13px;color:var(--muted);margin-top:2px}

/* gallery */
.tile{position:absolute;border-radius:6px}
.zoom{position:absolute;left:567px;top:3068px;width:68px;height:68px;border-radius:50%;background:var(--white)}

/* contact */
.input{position:absolute;border:1px solid #cfcfcf;font-size:14px;color:var(--text);padding:18px 0 0 28px}
.input span{color:#e0463b}
.submit{position:absolute;left:528px;top:4046px;width:144px;height:40px;background:var(--green);color:var(--white);font-family:"Poppins",Arial,sans-serif;font-weight:500;font-size:13.5px;display:flex;align-items:center;justify-content:center}

/* footer */
.site-footer{position:absolute;left:0;top:4163px;width:1200px;height:467px;background:linear-gradient(180deg,#1a9f80 0%,#168f73 55%,#137e66 100%);color:var(--white)}
.foot-logo{position:absolute;left:108px;top:72px;font-family:"Poppins",Arial,sans-serif;font-weight:700;font-size:25px}
.foot-about{position:absolute;left:111px;top:115px;width:250px;font-size:13.5px;line-height:26px}
.foot-head{position:absolute;top:74px;font-family:"Poppins",Arial,sans-serif;font-weight:600;font-size:20px}
.foot-list{position:absolute;top:118px;list-style:none;font-size:14.5px;line-height:25.7px}
.foot-list li{display:flex;align-items:center;gap:12px}
.foot-list.indent li.sub{padding-left:28px}
.copyright{position:absolute;top:4515px;font-size:13px;color:var(--white)}
.social-dot{position:absolute;top:4544px;width:23px;height:23px;border-radius:50%}
</style>
</head>
<body>
<div class="page">

  <header class="site-header">
    <div class="logo">Copper <span>Wren</span></div>
    <div class="nav active" style="left:463px">HOME</div>
    <div class="nav" style="left:535px">ABOUT US</div>
    <div class="nav" style="left:638px">PROPERTIES</div>
    <div class="nav" style="left:761px">REVIEWS</div>
    <div class="nav" style="left:858px">BLOG</div>
    <div class="nav" style="left:927px">CONTACT US</div>
    <div class="search-btn">
      <svg width="48" height="48" viewBox="0 0 48 48"><circle cx="23" cy="23" r="5" fill="none" stroke="#fff" stroke-width="2.2"/><line x1="27" y1="27" x2="31" y2="31" stroke="#fff" stroke-width="2.4" stroke-linecap="round"/></svg>
    </div>
  </header>

  <section class="hero" role="img" aria-label="Stone lodge with slate roof and garden at sunset">
    <h1 class="hero-title center">Copper Wren</h1>
    <div class="btn" style="left:516px;top:338px;width:168px;height:40px">GET STARTED
      <svg width="13" height="13" viewBox="0 0 14 14"><circle cx="7" cy="7" r="7" fill="#fff"/><path d="M5.5 4l3 3-3 3" stroke="#17a07f" stroke-width="1.8" fill="none"/></svg>
    </div>
    <div class="hero-arrow" style="left:60px">
      <svg width="46" height="46" viewBox="0 0 46 46"><path d="M25.5 18l-5 5 5 5" stroke="#222" stroke-width="2" fill="none"/></svg>
    </div>
    <div class="hero-arrow" style="left:1087px">
      <svg width="46" height="46" viewBox="0 0 46 46"><path d="M20.5 18l5 5-5 5" stroke="#222" stroke-width="2" fill="none"/></svg>
    </div>
    <svg class="abs" style="left:590px;top:530px" width="20" height="32" viewBox="0 0 20 32"><rect x="2" y="2" width="16" height="28" rx="8" fill="none" stroke="#fff" stroke-width="1.6"/><line x1="10" y1="8" x2="10" y2="13" stroke="#fff" stroke-width="1.6"/></svg>
  </section>

  <form class="booking">
    <label style="left:33px">Location</label>
    <label style="left:264px">Checkin</label>
    <label style="left:496px">Checkout</label>
    <div class="field" style="left:33px;width:217px"></div>
    <div class="field" style="left:264px;width:218px">
      <svg class="abs" style="right:10px;top:12px" width="14" height="14" viewBox="0 0 14 14"><rect x="1" y="2" width="12" height="11" fill="none" stroke="#fff" stroke-width="1.5"/><line x1="1" y1="5.5" x2="13" y2="5.5" stroke="#fff" stroke-width="1.5"/></svg>
    </div>
    <div class="field" style="left:496px;width:217px">
      <svg class="abs" style="right:10px;top:12px" width="14" height="14" viewBox="0 0 14 14"><rect x="1" y="2" width="12" height="11" fill="none" stroke="#fff" stroke-width="1.5"/><line x1="1" y1="5.5" x2="13" y2="5.5" stroke="#fff" stroke-width="1.5"/></svg>
    </div>
    <div class="book-now">BOOK NOW</div>
  </form>

  <section class="overview">
    <div class="photo" style="left:111px;top:948px;width:419px;height:433px;border:4px solid #fff;border-radius:10px;box-shadow:0 2px 8px rgba(0,0,0,.2);background:linear-gradient(180deg,#4d86d6 0%,#a9c7ec 30%,#8a9a6a 55%,#3ab0c6 72%,#6d7a45 100%)" role="img" aria-label="Backyard pool with palm trees under a blue sky"></div>
    <div class="photo" style="left:413px;top:1180px;width:153px;height:140px;border:4px solid #fff;border-radius:10px;box-shadow:0 2px 6px rgba(0,0,0,.2);background:linear-gradient(180deg,#c7d6e3 0%,#4f7f9a 45%,#6b6558 70%,#3a5a70 100%)" role="img" aria-label="Aerial view of lakeside homes and water"></div>
    <div class="eyebrow">OVERVIEW</div>
    <h2 class="heading abs" style="left:596px;top:970px;font-size:54px">Copper Wren</h2>
    <div class="rule" style="left:597px;top:1052px;width:117px"></div>
    <p class="para" style="left:599px;top:1079px;width:490px">Lorem ipsum dolor sit amet, consectetur adipiscing elit, sed do eiusmod tempor incididunt ut labore et dolore magna aliqua. Ut enim ad minim veniam, quis nostrud exercitation ullamco laboris nisi ut aliquip ex ea commodo consequat. Duis aute irure dolor in reprehenderit in voluptate velit esse cillum dolore eu fugiat nulla pariatur.</p>
    <p class="para" style="left:599px;top:1232px;width:490px">Excepteur sint occaecat cupidatat non proident, sunt in culpa qui officia deserunt mollit anim id est laborum. Lorem ipsum dolor sit amet, consecte tur adipiscing elit, sed do eiusmod tempor incididunt</p>
    <div class="btn" style="left:596px;top:1340px;width:168px;height:40px">LEARN MORE
      <svg width="13" height="13" viewBox="0 0 14 14"><circle cx="7" cy="7" r="7" fill="#fff"/><path d="M5.5 4l3 3-3 3" stroke="#17a07f" stroke-width="1.8" fill="none"/></svg>
    </div>
  </section>

  <section class="property-band">
    <h2 class="heading center abs" style="top:86px;font-size:54px;color:#fff">Our Property</h2>
    <div class="rule" style="left:543px;top:171px;width:114px;background:#fff"></div>
    <svg class="abs" style="left:40px;top:384px" width="28" height="44" viewBox="0 0 28 44"><path d="M22 4L6 22l16 18" stroke="#fff" stroke-width="3" fill="none"/></svg>
    <svg class="abs" style="left:1128px;top:384px" width="28" height="44" viewBox="0 0 28 44"><path d="M6 4l16 18L6 40" stroke="#fff" stroke-width="3" fill="none"/></svg>
  </section>

  <article class="card" style="left:111px;top:1688px;width:309px;height:399px">
    <div class="photo" style="left:6px;top:6px;width:297px;height:205px;border-radius:4px;background:linear-gradient(180deg,#3f6fa8 0%,#6a7e8a 50%,#2f5c70 80%,#24313b 100%)" role="img" aria-label="Modern home patio with dining table beside a pool at dusk"></div>
    <div class="prop-title">Nemo enim ipsam</div>
    <div class="prop-loc"><svg width="9" height="13" viewBox="0 0 9 13"><path d="M4.5 0a4.5 4.5 0 0 1 4.5 4.5C9 8 4.5 13 4.5 13S0 8 0 4.5A4.5 4.5 0 0 1 4.5 0z" fill="#17a07f"/><circle cx="4.5" cy="4.5" r="1.6" fill="#fff"/></svg>Architecto</div>
    <div class="prop-desc">Sed ut perspiciatis unde omnis iste natu serror sit Sed ut perspiciatis</div>
    <div class="prop-link">View details »</div>
  </article>
  <article class="card" style="left:445px;top:1688px;width:309px;height:399px">
    <div class="photo" style="left:6px;top:6px;width:297px;height:205px;border-radius:4px;background:linear-gradient(180deg,#7f9fb8 0%,#3c5a3a 40%,#5a3e2a 75%,#2a2420 100%)" role="img" aria-label="Wooden deck with lounge seating among tall pine trees"></div>
    <div class="prop-title">Nemo enim ipsam</div>
    <div class="prop-loc"><svg width="9" height="13" viewBox="0 0 9 13"><path d="M4.5 0a4.5 4.5 0 0 1 4.5 4.5C9 8 4.5 13 4.5 13S0 8 0 4.5A4.5 4.5 0 0 1 4.5 0z" fill="#17a07f"/><circle cx="4.5" cy="4.5" r="1.6" fill="#fff"/></svg>Architecto</div>
    <div class="prop-desc">Sed ut perspiciatis unde omnis iste natu serror sit Sed ut perspiciatis</div>
    <div class="prop-link">View details »</div>
  </article>
  <article class="card" style="left:779px;top:1688px;width:309px;height:399px">
    <div class="photo" style="left:6px;top:6px;width:297px;height:205px;border-radius:4px;background:linear-gradient(180deg,#c9cfc9 0%,#e6e6e2 35%,#4d7a3e 65%,#2f5a2a 100%)" role="img" aria-label="Aerial view of a white modern villa with pool among palms"></div>
    <div class="prop-title">Nemo enim ipsam</div>
    <div class="prop-loc"><svg width="9" height="13" viewBox="0 0 9 13"><path d="M4.5 0a4.5 4.5 0 0 1 4.5 4.5C9 8 4.5 13 4.5 13S0 8 0 4.5A4.5 4.5 0 0 1 4.5 0z" fill="#17a07f"/><circle cx="4.5" cy="4.5" r="1.6" fill="#fff"/></svg>Architecto</div>
    <div class="prop-desc">Sed ut perspiciatis unde omnis iste natu serror sit Sed ut perspiciatis</div>
    <div class="prop-link">View details »</div>
  </article>

  <section class="reviews">
    <h2 class="heading center abs" style="top:2278px;font-size:54px">Our Reviews</h2>
    <div class="rule" style="left:543px;top:2361px;width:114px"></div>
    <article class="review" style="left:111px">
      <div class="quote">“</div>
      <p>Lorem ipsum dolor sit amet, consec tetur adipiscing elit, sed do eiusmod tempor incididunt ut labore et dolore magna aliqua. Ut enim ad minim veniam, quis nostrud exercitation ullamco laboris nisi ut aliquip ex ea commodo consequat.</p>
      <hr>
      <div class="avatar" role="img" aria-label="Reviewer portrait"></div>
      <div class="reviewer">Ellis Marr<small>Copper Wren</small></div>
    </article>
    <article class="review featured" style="left:444px">
      <div class="quote">“</div>
      <p>Lorem ipsum dolor sit amet, consec tetur adipiscing elit, sed do eiusmod tempor incididunt ut labore et dolore magna aliqua. Ut enim ad minim veniam, quis nostrud exercitation ullamco laboris nisi ut aliquip ex ea commodo consequat.</p>
      <hr>
      <div class="avatar" role="img" aria-label="Reviewer portrait"></div>
      <div class="reviewer">Ellis Marr<small>Copper Wren</small></div>
    </article>
    <article class="review" style="left:776px">
      <div class="quote">“</div>
      <p>Lorem ipsum dolor sit amet, consec tetur adipiscing elit, sed do eiusmod tempor incididunt ut labore et dolore magna aliqua. Ut enim ad minim veniam, quis nostrud exercitation ullamco laboris nisi ut aliquip ex ea commodo consequat.</p>
      <hr>
      <div class="avatar" role="img" aria-label="Reviewer portrait"></div>
      <div class="reviewer">Ellis Marr<small>Copper Wren</small></div>
    </article>
  </section>

  <section class="gallery">
    <h2 class="heading center abs" style="top:2836px;font-size:54px">Our Gallery</h2>
    <div class="rule" style="left:543px;top:2918px;width:114px"></div>
    <div class="tile" style="left:18px;top:2958px;width:375px;height:600px;background:linear-gradient(180deg,#b9cde0 0%,#6f93b0 25%,#5b6d5e 50%,#556d3c 75%,#3f5a2c 100%)" role="img" aria-label="Aerial view of a coastal town along dunes and the sea"></div>
    <div class="tile" style="left:413px;top:2958px;width:375px;height:287px;background:linear-gradient(180deg,#8fb6e0 0%,#9c8a70 40%,#35b4d6 70%,#b58a6a 100%)" role="img" aria-label="Backyard pool with desert hillside behind"></div>
    <div class="zoom"><svg width="68" height="68" viewBox="0 0 68 68"><path d="M34 25v18M25 34h18" stroke="#222" stroke-width="4"/></svg></div>
    <div class="tile" style="left:806px;top:2958px;width:376px;height:287px;background:linear-gradient(160deg,#4b6a3a 0%,#8a7660 45%,#3d5a2e 100%)" role="img" aria-label="Aerial view of houses among trees in a neighbourhood"></div>
    <div class="tile" style="left:413px;top:3263px;width:769px;height:295px;background:linear-gradient(180deg,#6f8fb5 0%,#a08060 35%,#d8c8a8 60%,#3aa0c8 85%,#2a4a60 100%)" role="img" aria-label="Covered wooden patio overlooking a lit pool at dusk"></div>
  </section>

  <section class="contact">
    <h2 class="heading center abs" style="top:3646px;font-size:54px">Get in Touch</h2>
    <div class="input" style="left:269px;top:3752px;width:320px;height:52px">Name<span>*</span></div>
    <div class="input" style="left:607px;top:3752px;width:322px;height:52px">Email Address<span>*</span></div>
    <div class="input" style="left:269px;top:3827px;width:320px;height:52px">Phone<span>*</span></div>
    <div class="input" style="left:607px;top:3827px;width:322px;height:52px">Subject<span>*</span></div>
    <div class="input" style="left:269px;top:3897px;width:660px;height:128px;padding-top:26px">Message<span>*</span></div>
    <div class="submit">SUBMIT NOW</div>
  </section>

  <footer class="site-footer">
    <div class="foot-logo">Copper Wren</div>
    <p class="foot-about">Lorem ipsum dolor sit amet, consec tetur adipiscing elit, sed do eiusmod tempor incididunt ut labore et dolore magna aliqua. Lorem ipsum dolor sit amet, consectetur adipiscing</p>

    <div class="foot-head" style="left:440px">Information</div>
    <ul class="foot-list" style="left:441px">
      <li>» &nbsp;Home</li><li>» &nbsp;About us</li><li>» &nbsp;Services</li><li>» &nbsp;Blog</li><li>» &nbsp;Reviews</li><li>» &nbsp;Contact us</li>
    </ul>

    <div class="foot-head" style="left:668px">Contact</div>
    <ul class="foot-list indent" style="left:670px">
      <li><svg width="16" height="14" viewBox="0 0 16 14"><path d="M3 1l3 3-2 2c1 2 2.5 3.5 4.5 4.5l2-2 3 3-2 2C6 13 1 8 1 3z" fill="#fff"/></svg>Phone :</li>
      <li class="sub">+1 555 014 2290</li>
      <li><svg width="16" height="14" viewBox="0 0 16 14"><rect x="1" y="2" width="14" height="10" fill="#fff"/><path d="M1 2l7 5 7-5" stroke="#17a07f" stroke-width="1.4" fill="none"/></svg>Email :</li>
      <li class="sub">hello@copperwren.org</li>
      <li><svg width="16" height="14" viewBox="0 0 16 14"><path d="M8 0a4.5 4.5 0 0 1 4.5 4.5C12.5 8 8 14 8 14S3.5 8 3.5 4.5A4.5 4.5 0 0 1 8 0z" fill="#fff"/><circle cx="8" cy="4.5" r="1.6" fill="#17a07f"/></svg>Address</li>
      <li class="sub">48 Lakeside Row, Medicine Park</li>
    </ul>

    <div class="foot-head" style="left:964px">Follow us</div>
    <ul class="foot-list" style="left:966px;line-height:51px;top:105px">
      <li><svg width="10" height="10"><circle cx="5" cy="5" r="4" fill="#fff"/></svg>Gatherly</li>
      <li><svg width="10" height="10"><circle cx="5" cy="5" r="4" fill="#fff"/></svg>Chirpline</li>
      <li><svg width="10" height="10"><circle cx="5" cy="5" r="4" fill="#fff"/></svg>Snapframe</li>
    </ul>
  </footer>

  <div class="copyright center">© Copyrights 2022 Copper Wren | All Rights reserved</div>
  <div class="social-dot" style="left:538px;background:#3b5ea8"></div>
  <div class="social-dot" style="left:571px;background:#2aa3e0"></div>
  <div class="social-dot" style="left:604px;background:#d9453a"></div>
  <div class="social-dot" style="left:638px;background:#c9262f"></div>

</div>
</body>
</html>
```